Webdesign for starlight path

"Der Sternpfad" is a new info product that will be selled through the website maybe you will create for us.

Translated from german to english the project is named "the starlight path". It´s an online video course that teaches people how to live a fulfilling, happy and healthy life.

Design paramaters
We want a serious design that embodies the real feeling of beeing happy and fulfilled. Visitors should even feel good/better when they see the website.
In color psychology some sort of calming deep green like a four-leaf clover is recommend.
Mainly the website will be the external sales page with a big video as the central attention.
We also need a member area for customers to watch our video course.

So mainly we need a eye-cathing, calming header, the content body with mainly video and just a few written words...and of course a footer for links like imprint, affiliate program etc.

What we not want:
- some kind of these exaggerated smiling photos
- that bathetic luck symbols like money or boats

Hi,

i posted a message to the design discussion. Thank you!

```html
<!DOCTYPE html>
<html lang="en">
<head>
<meta charset="utf-8">
<title>Der Sternpfad – Online Video Course</title>
<link rel="stylesheet" href="https://fonts.googleapis.com/css2?family=Comfortaa:wght@300;400;700&family=Indie+Flower&display=swap">
<style>
  :root {
    --brand-blue: #1c8cc0;
    --text-teal: #4aa6c4;
    --headline-teal: #4aa8c2;
    --leaf-green: #8edc8a;
    --mint: #5ccf98;
    --aqua: #5fd6e0;
    --pale: #f3fbe9;
    --footer-mint: #c3f0d8;
    --footer-link: #5aaabb;
    --dark-blue-text: #0f4a8a;
    --player-black: #050505;
  }
  * { box-sizing: border-box; margin: 0; padding: 0; }
  html, body { width: 1200px; height: 720px; overflow: hidden; }
  body {
    position: relative;
    background: #ffffff;
    font-family: Arial, Helvetica, sans-serif;
  }

  .header-art {
    position: absolute; left: 0; top: 0; width: 1200px; height: 230px;
    background:
      radial-gradient(ellipse 180px 110px at 120px 60px, rgba(140,230,120,.8), transparent 70%),
      radial-gradient(ellipse 200px 120px at 620px 40px, rgba(100,220,235,.75), transparent 70%),
      radial-gradient(ellipse 160px 100px at 1120px 70px, rgba(90,210,230,.8), transparent 70%),
      radial-gradient(ellipse 220px 110px at 900px 90px, rgba(160,230,110,.6), transparent 70%),
      linear-gradient(180deg, #57c9a8 0%, #7fd9a8 35%, #cdeebb 70%, rgba(243,251,233,0) 100%);
  }

  .brand {
    position: absolute; left: 240px; top: 78px;
    display: flex; align-items: center; gap: 8px;
  }
  .brand-dot { width: 12px; height: 12px; border-radius: 50%; background: var(--brand-blue); }
  .brand-name {
    font-family: "Comfortaa", sans-serif; font-weight: 700;
    font-size: 23px; letter-spacing: 1px; color: var(--brand-blue);
  }

  .login { position: absolute; left: 701px; top: 38px; }
  .login-row { display: flex; align-items: center; gap: 5px; }
  .login-field {
    width: 110px; height: 18px; border-radius: 9px; border: none;
    background: #ffffff; color: var(--text-teal);
    font-size: 10px; text-align: center; line-height: 18px;
  }
  .login-go {
    width: 36px; height: 36px; border-radius: 50%; margin-left: 1px;
    background: #4cc6b4; color: #ffffff; font-size: 12px;
    display: flex; align-items: center; justify-content: center;
    box-shadow: 0 0 0 3px rgba(255,255,255,.35);
  }
  .login-options {
    display: flex; align-items: center; gap: 4px;
    margin: -6px 0 0 47px; font-size: 8.5px; color: var(--dark-blue-text);
  }
  .remember-box { width: 10px; height: 10px; background: #fff; border: 1px solid #6a9cc0; }

  .intro { position: absolute; left: 216px; top: 224px; width: 396px; }
  .intro-title {
    font-family: "Comfortaa", sans-serif; font-weight: 700;
    font-size: 26px; letter-spacing: 1.6px; color: var(--headline-teal);
    white-space: nowrap;
  }
  .intro-text {
    margin-top: 18px; font-size: 11.6px; line-height: 19.2px;
    color: var(--text-teal); text-align: justify; text-align-last: justify;
  }

  .buy-now {
    position: absolute; left: 346px; top: 422px; width: 176px; height: 87px;
    border-radius: 11px;
    background: linear-gradient(180deg, #8fe08c 0%, #6fd48e 55%, #5ccb98 100%);
    color: #ffffff; font-family: "Comfortaa", sans-serif; font-weight: 300;
    font-size: 28px; letter-spacing: 1.5px;
    display: flex; align-items: center; justify-content: center;
  }

  .video-label {
    position: absolute; left: 697px; top: 196px; width: 273px; text-align: center;
    font-family: "Indie Flower", cursive; font-size: 13px; color: #1a2a1a;
  }
  .video-player {
    position: absolute; left: 697px; top: 220px; width: 273px; height: 228px;
    background: var(--player-black); padding: 2px;
  }
  .video-screen {
    position: relative; width: 269px; height: 194px;
    background: radial-gradient(ellipse at 50% 35%, #e6f9df 0%, #aee8a2 45%, #62c96a 100%);
  }
  .video-screen svg { position: absolute; left: 118px; top: 80px; }
  .video-controls {
    position: absolute; left: 9px; top: 202px; width: 256px; height: 18px;
    background: linear-gradient(#fafafa, #d9d9d9);
    display: flex; align-items: center; font-size: 8px; font-weight: bold; color: #111;
  }
  .control-cell { height: 18px; display: flex; align-items: center; padding: 0 6px; border-right: 1px solid #bbb; }
  .progress { flex: 1; height: 4px; background: #9a9a9a; margin: 0 8px 0 4px; border-radius: 2px; }
  .video-shadow {
    position: absolute; left: 712px; top: 458px; width: 242px; height: 20px; border-radius: 50%;
    background: radial-gradient(ellipse, rgba(120,160,180,.35), transparent 70%);
  }

  .site-footer {
    position: absolute; left: 0; top: 661px; width: 1200px; height: 59px;
    background: linear-gradient(180deg, #bfeede 0%, #cdf2d2 60%, #daf6c8 100%);
  }
  .footer-nav {
    display: flex; justify-content: center; gap: 21px; padding: 0 0 0 20px; margin-top: 12px;
    list-style: none; font-size: 10px; color: var(--footer-link);
  }
</style>
</head>
<body>
  <div class="header-art" role="img" aria-label="Soft header illustration of floating green and aqua petals"></div>

  <div class="brand">
    <span class="brand-dot"></span>
    <span class="brand-name">Der Sternpfad</span>
  </div>

  <form class="login">
    <div class="login-row">
      <div class="login-field">username</div>
      <div class="login-field">password</div>
      <div class="login-go">go</div>
    </div>
    <div class="login-options">
      <span>remember me</span><span class="remember-box"></span><span>forgot password</span>
    </div>
  </form>

  <section class="intro">
    <h1 class="intro-title">Lorem ipsum dolor sit amet</h1>
    <p class="intro-text">Lorem ipsum dolor sit amet, consectetuer adipiscing elit, sed diam nonummy nibh euismod tincidunt ut laoreet dolore magna aliquam erat volutpat. Ut wisi enim ad minim veniam, quis nostrud exerci tation ullamcorper suscipit lobortis nisl ut aliquip ex ea commodo consequat. Duis autem vel eum iriure dolor in hendrerit in vulputate velit esse molestie consequat, vel illum dolore eu feugiat</p>
  </section>

  <div class="buy-now">Buy Now</div>

  <div class="video-label">watch video</div>
  <div class="video-player">
    <div class="video-screen" role="img" aria-label="Video poster with a soft multicoloured petal illustration">
      <svg width="42" height="46" viewBox="0 0 42 46"><path d="M0 0 L42 23 L0 46 Z" fill="#111"/></svg>
    </div>
    <div class="video-controls">
      <div class="control-cell"><svg width="7" height="8"><path d="M0 0 L7 4 L0 8Z" fill="#111"/></svg></div>
      <div class="control-cell" style="border:none">00:00</div>
      <div class="progress"></div>
      <div class="control-cell">00:00</div>
      <div class="control-cell">
        <svg width="26" height="8"><path d="M0 3h2l2-2v6l-2-2H0z" fill="#111"/><g stroke="#111"><line x1="9" y1="6" x2="9" y2="8"/><line x1="12" y1="5" x2="12" y2="8"/><line x1="15" y1="4" x2="15" y2="8"/><line x1="18" y1="3" x2="18" y2="8"/><line x1="21" y1="1" x2="21" y2="8"/><line x1="24" y1="0" x2="24" y2="8"/></g></svg>
      </div>
      <div class="control-cell" style="border:none">
        <svg width="8" height="8" fill="none" stroke="#111"><path d="M0 3V0h3M5 0h3v3M8 5v3H5M3 8H0V5"/></svg>
      </div>
    </div>
  </div>
  <div class="video-shadow"></div>

  <footer class="site-footer">
    <ul class="footer-nav">
      <li>ABOUT US</li><li>IMPRINT</li><li>AFFILIATE PROGRAM</li><li>CONTACT</li><li>HELP</li>
    </ul>
  </footer>
</body>
</html>
```